Mirela Hastow ADHD coach needs a flyer

I need a flyer to be sent by email. the copy is attached. It can be changed/reduced to fit the flyer. I would like to keep my website colors. My website is www.mirelahastow.example - Thank you!

```html
<!DOCTYPE html>
<html lang="en">
<head>
<meta charset="utf-8">
<title>Mirela Hastow – Academic Success Coaching Flyer</title>
<link rel="stylesheet" href="https://fonts.googleapis.com/css2?family=Montserrat:wght@800&family=Source+Sans+3:ital,wght@0,400;0,600;0,700;1,700&display=swap">
<style>
  :root {
    --teal: #6b96a2;
    --teal-dark: #5f8b98;
    --teal-light: #8fb2bd;
    --heading: #7fa5b1;
    --panel: #e8e8e8;
    --ink: #1c1c1c;
    --ink-soft: #2b2b2b;
    --cta-ink: #5b6b72;
    --backdrop: #4a4748;
    --paper: #ffffff;
  }
  * { margin: 0; padding: 0; box-sizing: border-box; }
  html, body { width: 883px; height: 1200px; overflow: hidden; }
  body {
    background: var(--backdrop);
    font-family: "Source Sans 3", "Myriad Pro", sans-serif;
    color: var(--ink);
  }
  .flyer {
    position: absolute;
    left: 28px; top: 0;
    width: 827px; height: 1200px;
    background: var(--paper);
    overflow: hidden;
  }
  .header-art { position: absolute; left: 0; top: 0; width: 827px; height: 1117px; }
  .title {
    position: absolute; left: 57px; top: 84px; width: 380px;
    font-family: "Montserrat", sans-serif; font-weight: 800;
    font-size: 30px; line-height: 40px; color: #fff;
  }
  .main-col { position: absolute; left: 51px; top: 417px; width: 414px; }
  .side-col { position: absolute; left: 517px; top: 410px; width: 292px; }

  .lead {
    font-style: italic; font-weight: 700; font-size: 18px; line-height: 21px;
    color: var(--ink); margin-bottom: 14px;
  }
  .body-copy { font-size: 12.2px; line-height: 15.4px; font-weight: 600; margin-bottom: 15px; }
  .section-title {
    font-family: "Montserrat", sans-serif; font-weight: 800;
    color: var(--heading); font-size: 20px; line-height: 24px;
  }
  .section-sub { color: var(--heading); font-weight: 700; font-size: 16.5px; line-height: 20px; margin-bottom: 9px; }
  .plain-copy { font-size: 12.2px; line-height: 14.6px; font-weight: 400; margin-bottom: 12px; }
  .list-title { color: var(--heading); font-weight: 700; font-size: 14px; margin-bottom: 6px; }

  .arrow-list { list-style: none; }
  .arrow-list li {
    position: relative; padding-left: 13px;
    font-size: 12.2px; line-height: 14.6px; margin-bottom: 6px;
  }
  .arrow-list li::before {
    content: ""; position: absolute; left: 0; top: 7px;
    border-left: 6px solid var(--teal-light);
    border-top: 3.5px solid transparent; border-bottom: 3.5px solid transparent;
  }
  .square-list { list-style: none; margin-bottom: 14px; }
  .square-list li {
    position: relative; padding-left: 10px;
    font-size: 12.2px; line-height: 14.6px; margin-bottom: 3.6px;
  }
  .square-list li::before {
    content: ""; position: absolute; left: 0; top: 6px;
    width: 4px; height: 4px; background: var(--teal-light);
  }
  .panel-title { color: var(--heading); font-weight: 700; font-size: 16px; line-height: 20px; margin-bottom: 6px; }
  .panel-sub { font-weight: 700; font-size: 13.5px; line-height: 16px; margin: 4px 0 12px; }
  .quote { font-size: 12.2px; line-height: 14.6px; margin-bottom: 12px; }
  .quote b { font-weight: 700; }
  .gap-lg { margin-top: 24px; }

  .next-steps {
    position: absolute; left: 68px; top: 1138px;
    display: flex; align-items: center;
  }
  .next-label { color: var(--heading); font-weight: 700; font-size: 22px; letter-spacing: 0.5px; }
  .chevrons { margin-left: 16px; }
  .next-text {
    margin-left: 20px; color: var(--cta-ink); font-weight: 700;
    font-size: 14.5px; line-height: 16px;
  }
</style>
</head>
<body>
<main class="flyer">
  <svg class="header-art" viewBox="0 0 827 1117" aria-hidden="false">
    <defs>
      <linearGradient id="photoTone" x1="0" y1="0" x2="0" y2="1">
        <stop offset="0" stop-color="#a7b0b2"/>
        <stop offset="0.55" stop-color="#c9b4b6"/>
        <stop offset="1" stop-color="#e9d3d6"/>
      </linearGradient>
    </defs>
    <rect class="side-panel" x="488" y="200" width="339" height="917" fill="var(--panel)"/>
    <path class="header-band" d="M0 0 H827 V223 Q690 150 560 260 Q470 320 300 360 Q150 390 0 397 Z" fill="var(--teal)"/>
    <path class="header-sweep" d="M0 325 Q250 305 540 220 L540 232 Q250 320 0 345 Z" fill="var(--teal-light)" opacity="0.45"/>
    <path class="header-sweep" d="M90 0 Q380 90 560 150 L560 170 Q360 105 60 0 Z" fill="var(--teal-light)" opacity="0.3"/>
    <circle cx="608" cy="210" r="177" fill="#fff"/>
    <circle cx="608" cy="210" r="165" fill="url(#photoTone)" role="img" aria-label="Portrait photograph of coach Mirela Hastow in a pale pink blazer"/>
  </svg>

  <h1 class="title">Helping Your Child with ADHD or Other Learning Challenges Thrive in College and Beyond</h1>

  <section class="main-col">
    <p class="lead">Academic success coaching that leads to lifelong transformation for students with ADHD and similar challenges that may have impeded their ability to thrive.</p>
    <p class="body-copy">Sending your child off to college can feel scary, especially if that college is hundreds of miles away. You worry about how they’ll do on their own—whether they’ll make friends, earn good grades, and be happy—especially without you there to support them daily. You know your child is bright, and you want them to have a great future, but you’re concerned they will struggle without the right support and resources.</p>
    <p class="body-copy">You don’t need to feel helpless as you send your child off to this next stage of their lives. Mirela is dedicated to making that transition easier for everyone. Mirela Hastow has years of experience helping students thrive despite their challenges. She sees your child’s potential and helps them see it, too. She provides a safety net as they adjust to a new environment at college. Her services are comprehensive and adaptable, based on the requirements of each individual: helping with course selection and scheduling, time management, study strategies, focus, making new friends, and adapting to change. Through it all, Mirela guides students through fundamental work on mindset to ensure that changes stick.</p>

    <h2 class="section-title" style="margin-top:4px">Empowering Focus:</h2>
    <p class="section-sub">How Mirela Helps</p>
    <p class="plain-copy">Mirela has taken students from failing to a 3.0 GPA, and from a C student to the Dean’s List, in just one semester. It doesn’t take years to provide lasting results; all it takes is the right guide.</p>
    <p class="list-title">Uniquely positioned to help your child, Mirela:</p>
    <ul class="arrow-list">
      <li>Tailors support so that your child improves focus and maximizes their potential in college and beyond.</li>
      <li>Understands your child’s unique needs - she sees the gifts that others often miss.</li>
      <li>Knows the academic landscape intimately, including the challenges faced by students with ADHD and other conditions.</li>
      <li>Helps with the logistics of scheduling in a way that most advisors can’t, enrolling students in the courses that best suit their learning style.</li>
      <li>Nurtures the brilliance in your bright child.</li>
      <li>Provides a balance between encouraging students and challenging them.</li>
    </ul>
  </section>

  <aside class="side-col">
    <h2 class="section-title">Realizing Potential:</h2>
    <p class="panel-sub">The Transformation You’ll<br>See in Your Child</p>
    <ul class="square-list">
      <li>A mindset of self-belief and increased confidence.</li>
      <li>Higher grades and the drive to graduate.</li>
      <li>Social integration and making friends.</li>
      <li>Happiness and fulfilment.</li>
      <li>A deep sense of personal achievement and pride.</li>
    </ul>
    <h3 class="panel-title">You Will Have:</h3>
    <ul class="square-list">
      <li>Less stress, knowing that your child is in good hands.</li>
      <li>Fewer sleepless nights worrying about your child.</li>
      <li>Confidence that they are receiving the right support.</li>
      <li>Joy and pride at seeing them do well.</li>
    </ul>
    <h3 class="panel-title gap-lg">What Parents Say</h3>
    <p class="quote">“Mirela was the glue that kept our daughter in college… as our daughter’s Academic Coach, [she] gave our daughter the ability to finish strong by empowering her with the skills needed to be successful.” -<b>Lorna</b></p>
    <p class="quote">“Mirela has always told my daughter not that she can succeed, but that she will succeed.”- <b>Patrice</b></p>
    <h3 class="panel-title">What Students Say</h3>
    <p class="quote">“Last semester I completed all 16 hours and I had the highest GPA I’ve ever had!” <b>-Former student</b></p>
    <p class="quote">“Under her instruction, my grades began to improve. I ended up making the Dean’s List during my time at Halvern, and I was also inducted into Sigma Tau Omicron. I am currently in my first year of law school at Westbrook University, a top tier school.”- <b>Former student</b></p>
  </aside>

  <footer class="next-steps">
    <span class="next-label">NEXT STEPS</span>
    <svg class="chevrons" width="52" height="30" viewBox="0 0 52 30" aria-hidden="true">
      <g fill="none" stroke="var(--teal-light)" stroke-width="1.6">
        <polyline points="2,2 12,15 2,28"/>
        <polyline points="14,2 24,15 14,28"/>
        <polyline points="26,2 36,15 26,28"/>
        <polyline points="38,2 48,15 38,28"/>
      </g>
    </svg>
    <p class="next-text">To learn more and discuss your child’s individual needs,<br>call 555·014·2273 or email coach@mirelahastow.example</p>
  </footer>
</main>
</body>
</html>
```